Restoration Specialist in need of business card designs

One side of the business card is a bathroom ripped out down to the studs with just a sink and toilet and then the other side is the bathroom (same sink and toilet) but put back together. Like a before and after on each side behind our information. Stand out, hard to forget, business cards for my restoration company. I want a unique concept all together.
Must include in no particular order:
our business name "Summit Renewals"
Possible Logo for a restoration company
Owner; Dennis Moravec
410-386-7294
dmoravec@summitrenewalsqx.example
SummitRenewalsQX.example (our company website) BUT I am open to any and all designs and options.

Target Market(s)

Customers, Men in the mitigation, plumbing, electrical, HVAC, Roofing, insurance companies

Industry/Entity Type

Restoration/ construction

Contact Information for Business Card

Must include in no particular order: our business name "Summit Renewals" Owner; Dennis Moravec 410-386-7294 dmoravec@summitrenewalsqx.example SummitRenewalsQX.example (our company website) MAY include a list of our services: Residential~ Emergency Response ~ Board- up~ Complete Restoration

Font styles to use
Serif

Colors
0054AA
0677BA
7BADD7
CADEEF
E8F1F8
F0912C
F2A743
F7CA91
FBE8D2
FDF5EE

Requirements
Must have
• unique, memorable, not something men have seen over and over again,
Nice to have
• eye catching
Should not have
• Been something I could have made by myself

```html
<!DOCTYPE html>
<html lang="en">
<head>
<meta charset="utf-8">
<title>Summit Renewals — Business Card</title>
<link rel="stylesheet" href="https://fonts.googleapis.com/css2?family=Bodoni+Moda:wght@400;500&display=swap">
<style>
  :root {
    --backdrop: #e6e6e6;
    --card: #ffffff;
    --ink: #1c1c1c;
    --icon-bg: #111111;
    --brand-orange: #f0912c;
    --band-pale: #cadeef;
    --band-blue: #0054aa;
    --band-accent: #f2a743;
  }
  * { margin: 0; padding: 0; box-sizing: border-box; }
  html, body {
    width: 1200px; height: 849px; overflow: hidden;
    background: var(--backdrop);
  }
  .canvas { position: relative; width: 1200px; height: 849px; }
  .card {
    position: absolute; left: 130px; top: 146px;
    width: 940px; height: 556px;
    background: var(--card);
    border-radius: 34px;
    overflow: hidden;
    font-family: "Bodoni Moda", "Times New Roman", serif;
    color: var(--ink);
    letter-spacing: 0.04em;
  }
  .card__bands { position: absolute; inset: 0; width: 940px; height: 556px; }
  .brand-name {
    position: absolute; left: 50px; top: 64px; width: 170px;
    text-align: center;
    font-size: 30px; font-weight: 500; line-height: 1.1;
    color: var(--brand-orange);
    letter-spacing: 0.02em;
  }
  .person { position: absolute; left: 32px; top: 266px; }
  .person__name {
    font-size: 31px; font-weight: 400; line-height: 1;
    text-decoration: underline; text-decoration-thickness: 1.5px;
    text-underline-offset: 4px;
  }
  .person__role { font-size: 21px; line-height: 1; margin-top: 4px; padding-left: 3px; }
  .contact { position: absolute; left: 20px; top: 359px; list-style: none; }
  .contact__item {
    display: flex; align-items: center; gap: 16px;
    height: 40px; margin-bottom: 27px;
    font-size: 21px;
  }
  .contact__item--email { font-size: 19.5px; letter-spacing: 0.03em; }
  .contact__icon {
    width: 40px; height: 40px; flex: none;
    border-radius: 50%; background: var(--icon-bg);
    display: flex; align-items: center; justify-content: center;
  }
  .services { position: absolute; left: 536px; top: 304px; }
  .services__title { font-size: 28px; font-weight: 400; padding-left: 16px; line-height: 1.2; }
  .services__list { list-style: none; font-size: 22px; line-height: 36px; }
</style>
</head>
<body>
<main class="canvas">
  <section class="card">
    <svg class="card__bands" viewBox="0 0 940 556" aria-hidden="true">
      <polygon fill="var(--band-pale)" points="660,0 940,0 940,556 880,556"/>
      <polygon fill="var(--band-blue)" points="760,0 940,0 940,556 905,556"/>
      <polygon fill="var(--band-accent)" points="840,0 870,0 930,556 915,556"/>
    </svg>

    <div class="brand-name">Summit<br>Renewals</div>

    <div class="person">
      <h1 class="person__name">Dennis Moravec</h1>
      <p class="person__role">Owner</p>
    </div>

    <ul class="contact">
      <li class="contact__item">
        <span class="contact__icon">
          <svg width="20" height="20" viewBox="0 0 24 24"><path fill="#fff" d="M6.6 10.8a15.1 15.1 0 0 0 6.6 6.6l2.2-2.2a1 1 0 0 1 1-.25 11.4 11.4 0 0 0 3.6.57 1 1 0 0 1 1 1V20a1 1 0 0 1-1 1A17 17 0 0 1 3 4a1 1 0 0 1 1-1h3.5a1 1 0 0 1 1 1c0 1.25.2 2.450.57 3.57a1 1 0 0 1-.25 1z"/></svg>
        </span>
        <span>410-386-7294</span>
      </li>
      <li class="contact__item contact__item--email">
        <span class="contact__icon">
          <svg width="20" height="20" viewBox="0 0 24 24"><rect x="3" y="6" width="18" height="12" fill="none" stroke="#fff" stroke-width="1.6"/><path d="M3 6l9 7 9-7" fill="none" stroke="#fff" stroke-width="1.6"/></svg>
        </span>
        <span>dmoravec@summitrenewalsqx.example</span>
      </li>
      <li class="contact__item">
        <span class="contact__icon">
          <svg width="20" height="20" viewBox="0 0 24 24" fill="none" stroke="#fff" stroke-width="1.4"><circle cx="12" cy="12" r="8.5"/><ellipse cx="12" cy="12" rx="3.8" ry="8.5"/><path d="M3.5 12h17M5 8h14M5 16h14"/></svg>
        </span>
        <span>SummitRenewalsQX.example</span>
      </li>
    </ul>

    <div class="services">
      <h2 class="services__title">Services:</h2>
      <ul class="services__list">
        <li>- Residential</li>
        <li>- Emergency Response</li>
        <li>- Board- up</li>
        <li>- Storm Protection</li>
        <li>- Complete Restoration</li>
      </ul>
    </div>
  </section>
</main>
</body>
</html>
```